Design a fresh new presentation folder for us!

We are looking for a fresh design of our new presentation folder.<br/><br/>We would like our current logo and colours being used in the design as well as images associated with our industry being international logistics.<br/><br/>Our services include, international freight - sea and air, domestic road transport, 3pl and warehousing.<br/><br/>We will attach our logo and other images we have used in the past to give you an idea of what we are after. Also attached our old folder.<br/><br/>We want a brand new fresh approach that is a really modern design. It needs to be visually striking.

Industry/Entity Type

Logistic

Colors
9ccb3b
acd037
cadf82
eef4d8

Requirements
Must have
• Fresh. Modern. Visually striking. Industry related.
• Slogan - Local Knowledge, Global Strength or Complete Logistics Solutions

```html
<!DOCTYPE html>
<html lang="en">
<head>
<meta charset="utf-8">
<title>Norvale Logistics Group – Presentation Folder</title>
<link href="https://fonts.googleapis.com/css2?family=Lato:ital,wght@0,400;0,700;0,900;1,900&display=swap" rel="stylesheet">
<style>
:root{
  --green:#9ccb3b;
  --green-2:#acd037;
  --green-light:#cadf82;
  --green-pale:#eef4d8;
  --green-dark:#5e9a1f;
  --grey:#8a8c90;
  --grey-dark:#555a60;
  --paper:#f4f5f6;
  --bg:#e4e5e7;
  --ink:#3b3f44;
}
*{box-sizing:border-box;margin:0;padding:0}
html,body{width:850px;height:1200px;overflow:hidden}
body{background:var(--bg);font-family:"Lato",sans-serif;color:var(--ink);position:relative}
.spread{position:absolute;left:65px;width:720px;height:480px;display:flex;box-shadow:0 10px 30px rgba(0,0,0,.18)}
.spread--outer{top:60px}
.spread--inner{top:680px}
.panel{position:relative;width:360px;height:480px;overflow:hidden;background:var(--paper)}
.panel + .panel{border-left:1px solid #d6d8da}
.panel svg.art{position:absolute;inset:0;width:100%;height:100%}
.label{position:absolute;font-weight:900;font-style:italic;font-size:48px;color:var(--grey);letter-spacing:1px}
.label--outer{top:548px;right:85px}
.label--inner{top:610px;left:85px}

/* wordmark */
.wordmark{position:absolute;display:flex;align-items:center;gap:8px;color:var(--green-dark);font-weight:900}
.wordmark .mark-dot{width:12px;height:12px;background:var(--green)}
.wordmark .name{font-size:30px;letter-spacing:1px}
.wordmark .sub{font-size:11px;line-height:1.15;font-weight:900;letter-spacing:1.5px;border-left:1px solid var(--grey);padding-left:8px;text-transform:uppercase}

/* outer back */
.back .wordmark{left:28px;bottom:62px}
.back .wordmark .name{font-size:24px}
.back .wordmark .sub{font-size:9px}
.back .address{position:absolute;right:22px;bottom:70px;text-align:right;font-size:8px;font-weight:700;line-height:1.35;color:var(--grey-dark)}
.contact-bar{position:absolute;left:0;right:0;bottom:18px;height:28px;background:var(--grey);color:#fff;font-size:10px;display:flex;align-items:center;padding-left:24px;letter-spacing:.3px}

/* outer front */
.front .slogan{position:absolute;top:26px;right:22px;text-align:right;color:#fff;font-size:17px;line-height:1.1;text-shadow:0 1px 3px rgba(0,0,0,.35)}
.front .slogan b{font-weight:900;color:var(--green-pale)}
.front .wordmark{left:70px;top:300px}
.tagline-bar{position:absolute;left:30px;right:0;top:372px;height:26px;background:var(--grey);color:#fff;font-size:10.5px;display:flex;align-items:center;justify-content:center;letter-spacing:.5px;text-transform:uppercase}

/* inner left */
.photo-stack{position:absolute;left:16px;top:22px;width:152px;display:flex;flex-direction:column;gap:8px}
.photo-stack .photo{height:98px;border:3px solid #fff;box-shadow:0 1px 3px rgba(0,0,0,.2)}
.ghost-name{position:absolute;left:200px;top:60px;font-weight:900;font-size:120px;color:rgba(130,136,140,.25);transform:rotate(90deg);transform-origin:left top;left:300px;letter-spacing:4px}

/* inner right */
.tables{position:absolute;top:16px;left:14px;right:14px;display:flex;gap:10px}
.tables .col{display:flex;flex-direction:column;gap:8px}
.tables .col:first-child{width:140px}
.tables .col:last-child{flex:1}
table.conv{width:100%;border-collapse:collapse;font-size:6px;color:var(--ink)}
table.conv th{background:var(--green);color:#fff;font-weight:900;padding:2px 3px;text-align:right}
table.conv th:first-child{text-align:center}
table.conv td{padding:1.4px 3px;border-bottom:1px solid #fff}
table.conv td:first-child{text-align:right}
table.conv td:last-child{width:38px;background:#fff;border-left:2px solid var(--paper)}
table.conv tr:nth-child(odd) td:first-child{background:var(--green-light)}
table.conv tr:nth-child(even) td:first-child{background:var(--green-pale)}
.truck-photo{position:absolute;left:30px;right:0;top:196px;height:150px}
.pocket{position:absolute;left:0;right:0;bottom:0;height:175px;background:var(--green);display:flex;align-items:center;justify-content:center}
.pocket .pocket-address{color:#fff;font-size:7px;line-height:1.45;text-align:center}
.pocket .slit{position:absolute;top:62px;width:22px;height:1px;background:rgba(255,255,255,.7)}
.pocket .slit--l{left:108px;transform:rotate(-30deg)}
.pocket .slit--r{right:108px;transform:rotate(30deg)}
</style>
</head>
<body>

<!-- OUTER SPREAD -->
<section class="spread spread--outer">
  <div class="panel back">
    <svg class="art" viewBox="0 0 360 480" preserveAspectRatio="none">
      <defs>
        <linearGradient id="backPhoto" x1="0" y1="0" x2="0" y2="1">
          <stop offset="0" stop-color="#a9c79a"/>
          <stop offset=".5" stop-color="#2f4a6b"/>
          <stop offset="1" stop-color="#8ea07a"/>
        </linearGradient>
        <linearGradient id="swooshB" x1="0" y1="1" x2="1" y2="0">
          <stop offset="0" stop-color="#6fa62a"/>
          <stop offset=".6" stop-color="#9ccb3b"/>
          <stop offset="1" stop-color="#cadf82"/>
        </linearGradient>
        <linearGradient id="mapSoft" x1="0" y1="0" x2="1" y2="1">
          <stop offset="0" stop-color="#eef0f3"/>
          <stop offset="1" stop-color="#dfe5ec"/>
        </linearGradient>
      </defs>
      <rect width="360" height="480" fill="url(#mapSoft)" role="img" aria-label="Faint world map with connection lines"/>
      <path d="M0,0 L320,0 C260,150 120,260 0,300 Z" fill="url(#backPhoto)" role="img" aria-label="Photo of a container ship docked under port cranes"/>
      <path d="M320,0 L360,0 L360,40 C300,210 150,330 0,372 L0,300 C120,260 260,150 320,0 Z" fill="url(#swooshB)"/>
      <path d="M360,40 C300,210 150,330 0,372 L0,380 C150,338 304,214 360,52 Z" fill="#a7a9ac"/>
      <rect x="0" y="476" width="360" height="4" fill="var(--green)"/>
    </svg>
    <div class="wordmark"><span class="mark-dot"></span><span class="name">NVL</span><span class="sub">Norvale<br>Logistics<br>Group</span></div>
    <p class="address">4/118 Harbourline Road<br>Portside, NSW, 2031.<br>PO Box 2207<br>Portside, NSW, 1480</p>
    <div class="contact-bar">T: +61 2 9400 1234 &nbsp;|&nbsp; F: +61 2 9400 5678 &nbsp;|&nbsp; www.norvalelogistics.com</div>
  </div>

  <div class="panel front">
    <svg class="art" viewBox="0 0 360 480" preserveAspectRatio="none">
      <defs>
        <linearGradient id="frontPhoto" x1="0" y1="0" x2="1" y2="1">
          <stop offset="0" stop-color="#6fa8a0"/>
          <stop offset=".5" stop-color="#c9744a"/>
          <stop offset="1" stop-color="#f0c070"/>
        </linearGradient>
        <linearGradient id="swooshF" x1="0" y1="0" x2="1" y2="1">
          <stop offset="0" stop-color="#cadf82"/>
          <stop offset=".5" stop-color="#9ccb3b"/>
          <stop offset="1" stop-color="#6fa62a"/>
        </linearGradient>
      </defs>
      <rect width="360" height="480" fill="url(#mapSoft)" role="img" aria-label="Faint world map with connection lines"/>
      <path d="M40,0 L360,0 L360,230 C240,215 110,160 40,0 Z" fill="url(#frontPhoto)" role="img" aria-label="Photo of a plane flying over a container yard at sunset"/>
      <path d="M0,0 L40,0 C110,160 240,215 360,230 L360,272 C220,262 70,210 0,50 Z" fill="url(#swooshF)"/>
      <path d="M0,50 C70,210 220,262 360,272 L360,280 C220,270 68,218 0,62 Z" fill="#a7a9ac"/>
      <rect x="0" y="476" width="360" height="4" fill="var(--green)"/>
    </svg>
    <p class="slogan">Local <b>Knowledge</b><br>Global <b>Strength</b></p>
    <div class="wordmark"><span class="mark-dot"></span><span class="name">NVL</span><span class="sub">Norvale<br>Logistics<br>Group</span></div>
    <div class="tagline-bar">A world of experience at your fingertips</div>
  </div>
</section>
<p class="label label--outer">OUTER</p>

<!-- INNER SPREAD -->
<p class="label label--inner">INNER</p>
<section class="spread spread--inner">
  <div class="panel inner-left">
    <svg class="art" viewBox="0 0 360 480" preserveAspectRatio="none">
      <defs>
        <linearGradient id="innerBg" x1="0" y1="0" x2="0" y2="1">
          <stop offset="0" stop-color="#eef4d8"/>
          <stop offset=".6" stop-color="#f4f5f6"/>
          <stop offset="1" stop-color="#9ccb3b"/>
        </linearGradient>
      </defs>
      <rect width="360" height="480" fill="url(#innerBg)"/>
      <rect width="360" height="480" fill="url(#innerBg)" opacity="0"/>
      <path d="M0,400 C120,380 240,420 360,395 L360,480 L0,480 Z" fill="#7fb531" opacity=".45"/>
      <path d="M0,440 C140,420 250,450 360,430 L360,436 C250,456 140,426 0,446 Z" fill="#fff" opacity=".6"/>
    </svg>
    <span class="ghost-name">NVL</span>
    <div class="photo-stack">
      <div class="photo" role="img" aria-label="Photo of a worker checking stock in a warehouse aisle" style="background:linear-gradient(135deg,#c98a5a,#e9c7a0)"></div>
      <div class="photo" role="img" aria-label="Photo of stacked shipping containers at dusk" style="background:linear-gradient(160deg,#4a6fa0,#2b3d5a)"></div>
      <div class="photo" role="img" aria-label="Photo of wrapped air cargo beside an aircraft engine" style="background:linear-gradient(160deg,#8f9aa6,#4b5560)"></div>
      <div class="photo" role="img" aria-label="Photo of tall warehouse racking filled with boxes" style="background:linear-gradient(160deg,#a59078,#5d6b7a)"></div>
    </div>
  </div>

  <div class="panel inner-right">
    <div class="tables">
      <div class="col">
        <table class="conv">
          <tr><th>Length</th><th>Multiply By</th></tr>
          <tr><td>Inches to Centimetres</td><td>2.54</td></tr>
          <tr><td>Centimetres to Inches</td><td>0.39</td></tr>
          <tr><td>Inches to Millimetres</td><td>25.40</td></tr>
          <tr><td>Millimetres to Inches</td><td>0.04</td></tr>
          <tr><td>Feet to Metres</td><td>0.31</td></tr>
          <tr><td>Metres to Feet</td><td>3.28</td></tr>
        </table>
        <table class="conv">
          <tr><th>Weight</th><th>Multiply By</th></tr>
          <tr><td>Pounds to Kilograms</td><td>0.45</td></tr>
          <tr><td>Kilograms to Pounds</td><td>2.21</td></tr>
          <tr><td>Ounces to Grams</td><td>28.35</td></tr>
          <tr><td>Grams to Ounces</td><td>0.04</td></tr>
          <tr><td>Long Tons to Tonnes</td><td>1.02</td></tr>
          <tr><td>Tonnes to Long Tons</td><td>0.98</td></tr>
          <tr><td>Short Tons to Tonnes</td><td>0.91</td></tr>
          <tr><td>Tonnes to Short Tons</td><td>1.10</td></tr>
        </table>
      </div>
      <div class="col">
        <table class="conv">
          <tr><th>Area</th><th>Multiply By</th></tr>
          <tr><td>Square Inches to Square Centimetres</td><td>6.452</td></tr>
          <tr><td>Square Centimetres to Square Inches</td><td>0.15</td></tr>
          <tr><td>Square Feet to Square Metres</td><td>0.09</td></tr>
          <tr><td>Square Metres to Square Feet</td><td>10.76</td></tr>
          <tr><td>Square Yards to Square Metres</td><td>0.84</td></tr>
        </table>
        <table class="conv">
          <tr><th>Volume</th><th>Multiply By</th></tr>
          <tr><td>Cubic Inches to Cubic Centimetres</td><td>16.39</td></tr>
          <tr><td>Cubic Centimetres to Cubic Inches</td><td>0.06</td></tr>
          <tr><td>Cubic Feet to Cubic Metres</td><td>0.03</td></tr>
          <tr><td>Cubic Metres to Cubic Feet</td><td>35.32</td></tr>
          <tr><td>Cubic Yards to Cubic Metres</td><td>0.76</td></tr>
          <tr><td>Cubic Metres to Cubic Yards</td><td>1.31</td></tr>
          <tr><td>Cubic Inches to Litres</td><td>0.02</td></tr>
          <tr><td>Litres to Cubic Inches</td><td>61.03</td></tr>
        </table>
      </div>
    </div>
    <div class="truck-photo" role="img" aria-label="Photo of a white semi-trailer truck in green and grey tones" style="background:linear-gradient(120deg,#6d8a5a,#e8ece4 55%,#cfd6c8)"></div>
    <div class="pocket">
      <span class="slit slit--l"></span><span class="slit slit--r"></span>
      <p class="pocket-address">1450 Meridian Way, Suite 310<br>Lakeport, MI 48501<br>Tel: 555 210-4477<br>www.folderworks.example</p>
    </div>
  </div>
</section>

</body>
</html>
```